Flayer design for American style Pizza Company

We need to enhance an A5 flayer which we didn’t print yet because it doesn’t look good. We will send the file to the designer (PSD format) and we need a design that look like a fast food companies (QRB, Grill Meadow, Tolvins ,,etc.). Also some products picture which are included in the file needs to be improved (brightness , contrast, size, etc.). We may also provied the origenal master photos for the products.

please download the main files from http://dropvault.example/xKqTmwRzaP

Please dowload Products Pictures from http://dropvault.example/p4hWseLc7D

please download the main files from     http://dropvault.example/xKqTmwRzaP                     

hi all

Best Regards       

                                   

                                        Please dowload Products Pictures from     http://dropvault.example/p4hWseLc7D     

                                   

Reason: Hi all I guarantee to accept the design which sticks with the requirements. The submitted design will be compared before approval with ,Grill Meadow, QRB, Crust Barn etc designs. GoodLuck all Best Regards

```html
<!DOCTYPE html>
<html lang="ar">
<head>
<meta charset="utf-8">
<title>Tortilla Flyer – Front and Back</title>
<link href="https://fonts.googleapis.com/css2?family=Cairo:wght@700;800;900&family=Arimo:wght@700&display=swap" rel="stylesheet">
<style>
  :root {
    --red: #e01e26;
    --red-deep: #c8141c;
    --orange: #f7931e;
    --orange-light: #fbb03b;
    --green: #3aa145;
    --white: #ffffff;
    --text-red: #e3222a;
    --backdrop: #dcd8d1;
  }
  * { box-sizing: border-box; margin: 0; padding: 0; }
  html, body { width: 1200px; height: 870px; overflow: hidden; }
  body { background: var(--backdrop); position: relative; font-family: "Cairo", sans-serif; }

  .flyer {
    position: absolute; top: 76px; width: 535px; height: 759px; overflow: hidden;
    background: radial-gradient(ellipse 70% 55% at 50% 50%, var(--orange-light) 0%, var(--orange) 40%, var(--red) 85%);
    box-shadow: 0 3px 10px rgba(0,0,0,.35);
  }
  .flyer--front { left: 33px; }
  .flyer--back { left: 633px; }

  .ribbon { position: absolute; left: 40px; top: 35px; width: 455px; height: 95px; }
  .ribbon__text {
    position: absolute; left: 70px; top: 78px; width: 395px; text-align: center;
    color: var(--white); font-weight: 900; font-size: 31px; line-height: 1;
    white-space: nowrap; transform: translateY(-50%);
  }

  .product-card {
    position: absolute; left: 37px; width: 460px;
    background: var(--white); border: 2px solid var(--red); border-radius: 10px;
    box-shadow: 0 0 0 3px rgba(255,255,255,.35);
  }
  .product-card__name {
    position: absolute; left: 16px; top: 50%; transform: translateY(-50%);
    width: 170px; text-align: center; direction: rtl; white-space: nowrap;
    color: var(--text-red); font-weight: 800; font-size: 38px; line-height: 1.3;
  }
  .product-card--wide-name .product-card__name { width: 215px; left: 10px; }
  .product-card__photo {
    position: absolute; right: 10px; top: 8px; bottom: 8px; width: 265px; border-radius: 6px;
    background: radial-gradient(ellipse at 50% 65%, #e2b87a 0%, #c98a4a 45%, #f4ede4 80%);
  }
  .product-card--wide-name .product-card__photo { width: 225px; }
  .badge-new {
    position: absolute; right: 22px; top: 14px; width: 44px; height: 44px; border-radius: 50%;
    background: var(--green); border: 2px solid var(--white); color: var(--white);
    font-weight: 800; font-size: 14px; line-height: 40px; text-align: center;
  }

  .promo-band { position: absolute; left: 0; top: 492px; width: 100%; height: 153px; background: var(--green); }
  .promo-oval {
    position: absolute; left: 30px; top: 452px; width: 475px; height: 186px; border-radius: 50%;
    background: radial-gradient(ellipse at 50% 45%, #ee2a30 0%, var(--red-deep) 80%);
    border: 3px solid var(--orange-light);
  }
  .promo-oval__text {
    position: absolute; left: 0; right: 0; top: 58px; text-align: center; direction: rtl; white-space: nowrap;
    color: var(--white); font-weight: 800; font-size: 38px; line-height: 1.25;
  }
  .halal-seal {
    position: absolute; left: 245px; top: 448px; width: 46px; height: 46px; border-radius: 50%;
    background: var(--red); border: 3px solid var(--white);
  }

  .footer { position: absolute; left: 0; bottom: 0; width: 100%; height: 113px; background: var(--red); }
  .footer__brand-zone {
    position: absolute; right: 0; top: 0; width: 215px; height: 100%;
    background: linear-gradient(90deg, var(--white) 0%, #a8d6a6 45%, var(--green) 100%);
  }
  .footer__label {
    position: absolute; left: 18px; top: 12px; color: var(--white);
    font-family: "Arimo", sans-serif; font-weight: 700; font-size: 13px; white-space: nowrap;
  }
  .footer__label span { font-family: "Cairo", sans-serif; margin-left: 6px; }
  .footer__phone {
    position: absolute; left: 16px; top: 30px; color: var(--white); white-space: nowrap;
    font-family: "Arimo", sans-serif; font-weight: 700; font-size: 47px; letter-spacing: 1px;
  }
  .brand {
    position: absolute; right: 14px; top: 34px; display: flex; align-items: center; gap: 8px;
    direction: rtl; color: var(--text-red); font-weight: 900; font-size: 27px; line-height: 1; white-space: nowrap;
  }
  .brand__dot { width: 22px; height: 22px; border-radius: 50%; background: var(--text-red); }
</style>
</head>
<body>

<section class="flyer flyer--front" aria-label="Flyer front">
  <svg class="ribbon" viewBox="0 0 455 95" aria-hidden="true">
    <polygon points="0,30 45,22 45,84 0,90 18,60" fill="#b5121a" stroke="#fbb03b" stroke-width="3"/>
    <polygon points="455,24 410,16 410,78 455,86 437,54" fill="#b5121a" stroke="#fbb03b" stroke-width="3"/>
    <path d="M25,14 Q228,-4 430,8 L430,72 Q228,60 25,82 Z" fill="#e01e26" stroke="#fbb03b" stroke-width="4"/>
  </svg>
  <div class="ribbon__text" dir="rtl">ابدأ يومك بفطائر التورتيلا</div>

  <article class="product-card" style="top:157px;height:130px">
    <h2 class="product-card__name">تورتيلا<br>الفلافل</h2>
    <div class="product-card__photo" role="img" aria-label="Grilled falafel tortilla wraps with tomato, falafel and greens"></div>
    <div class="badge-new" dir="rtl">جديد</div>
  </article>

  <article class="product-card" style="top:305px;height:130px">
    <h2 class="product-card__name">تورتيلا<br>الدجاج</h2>
    <div class="product-card__photo" role="img" aria-label="Grilled chicken tortilla wraps with shredded cheese and lettuce"></div>
  </article>

  <div class="promo-band"></div>
  <div class="promo-oval"><p class="promo-oval__text">تورتيلا محمصة تصلك<br>ساخنة وهشة</p></div>
  <div class="halal-seal"></div>

  <footer class="footer">
    <p class="footer__label">Fast delivery service <span dir="rtl">خدمة توصيل سريعة</span></p>
    <p class="footer__phone">037 555 910</p>
    <div class="footer__brand-zone">
      <div class="brand"><span>فورنو بيتزا</span><span class="brand__dot"></span></div>
    </div>
  </footer>
</section>

<section class="flyer flyer--back" aria-label="Flyer back">
  <article class="product-card" style="top:21px;height:128px">
    <h2 class="product-card__name">تورتيلا<br>التونا</h2>
    <div class="product-card__photo" role="img" aria-label="Tuna tortilla wraps with green pepper, red onion and black olives"></div>
  </article>
  <article class="product-card" style="top:177px;height:128px">
    <h2 class="product-card__name">تورتيلا<br>الفيتا</h2>
    <div class="product-card__photo" role="img" aria-label="Feta tortilla wraps with tomato, feta cubes and herbs"></div>
  </article>
  <article class="product-card product-card--wide-name" style="top:332px;height:129px">
    <h2 class="product-card__name">تورتيلا لبنة<br>زعتر</h2>
    <div class="product-card__photo" role="img" aria-label="Labneh and zaatar tortilla wraps with a bowl of labneh"></div>
  </article>
  <article class="product-card" style="top:487px;height:130px">
    <h2 class="product-card__name">تورتيلا<br>الجبنة</h2>
    <div class="product-card__photo" role="img" aria-label="Cheese tortilla wraps with tomato, cucumber and olives"></div>
  </article>

  <footer class="footer">
    <p class="footer__label">Fast delivery service <span dir="rtl">خدمة توصيل سريعة</span></p>
    <p class="footer__phone">037 555 910</p>
    <div class="footer__brand-zone">
      <div class="brand"><span>فورنو بيتزا</span><span class="brand__dot"></span></div>
    </div>
  </footer>
</section>

</body>
</html>
```